Business Stationery Design

I would like to get some stationery designed for my company. The stationery should include a letterhead, envelope, and business card. We are a technology consulting company specializing in Healthcare IT, and Education management systems. The colors of the stationery should match the logo. The logo is uploaded.

Target Market(s)

Hospitals, Clinics. Doctors offices. Private Schools.

Industry/Entity Type

Business

```html
<!DOCTYPE html>
<html lang="en">
<head>
<meta charset="utf-8">
<title>Larchfield Advisory Group – Business Card</title>
<link rel="stylesheet" href="https://fonts.googleapis.com/css2?family=Roboto:wght@400;500&family=Roboto+Condensed:wght@500&display=swap">
<style>
  :root {
    --backdrop: #2a2a2a;
    --brand-green: #76bc2c;
    --brand-green-edge: #6aab25;
    --brand-orange: #f5b400;
    --card-white: #f3f3f3;
    --ink: #4a4a4a;
    --on-green: #ffffff;
  }
  * { margin: 0; padding: 0; box-sizing: border-box; }
  html, body { width: 1200px; height: 960px; overflow: hidden; }
  body {
    background: var(--backdrop);
    position: relative;
    font-family: "Roboto", Arial, sans-serif;
  }
  .card {
    position: absolute;
    left: 320px;
    width: 600px;
    height: 342px;
    border-radius: 18px;
  }
  .card-back {
    top: 108px;
    background: var(--brand-green);
    color: var(--on-green);
    box-shadow: 0 8px 0 var(--brand-green-edge);
  }
  .card-back .brand {
    position: absolute;
    left: 0; right: 0; top: 80px;
    display: flex; flex-direction: column; align-items: center; gap: 14px;
    font-size: 34px; font-weight: 500; line-height: 1;
  }
  .card-back .brand-dot {
    width: 100px; height: 100px; border-radius: 50%;
    background: var(--on-green);
  }
  .card-back .website {
    position: absolute;
    left: 0; right: 0; top: 288px;
    text-align: center;
    font-size: 14px;
    letter-spacing: 4.5px;
  }
  .card-front {
    top: 493px;
    background: var(--card-white);
  }
  .card-front .brand {
    position: absolute;
    left: 32px; top: 30px;
    width: 200px;
    display: flex; flex-direction: column; align-items: center; gap: 14px;
    color: var(--brand-green);
    font-size: 26px; font-weight: 400;
    line-height: 1.15;
    text-align: center;
  }
  .card-front .brand-dot {
    width: 100px; height: 100px; border-radius: 50%;
    background: var(--brand-orange);
    flex: none;
  }
  .contact {
    position: absolute;
    right: 30px; top: 122px;
    text-align: right;
    color: var(--ink);
    font-size: 14.5px;
  }
  .contact .name {
    font-family: "Roboto Condensed", Arial, sans-serif;
    font-weight: 500;
    font-size: 22px;
    color: var(--brand-green);
    line-height: 26px;
  }
  .contact .role {
    font-weight: 500;
    font-size: 14px;
    color: var(--brand-orange);
    line-height: 20px;
    margin-bottom: 6px;
  }
  .contact .address { line-height: 19px; margin-bottom: 8px; }
  .contact-list { list-style: none; }
  .contact-list li {
    display: flex; justify-content: flex-end; align-items: center;
    gap: 8px; line-height: 19.5px;
  }
  .contact-list svg { width: 14px; height: 14px; fill: var(--brand-green); flex: none; }
</style>
</head>
<body>
  <section class="card card-back">
    <div class="brand"><span class="brand-dot"></span><span>Larchfield</span></div>
    <p class="website">www.larchfield.com</p>
  </section>

  <section class="card card-front">
    <div class="brand"><span class="brand-dot"></span><span>Larchfield<br>Advisory Group</span></div>
    <div class="contact">
      <p class="name">OWEN CARTER</p>
      <p class="role">CEO/FOUNDER</p>
      <p class="address">4312 Juniper Court<br>Fairbanks, Alaska 56210</p>
      <ul class="contact-list">
        <li>512 308 7741
          <svg viewBox="0 0 16 16"><path d="M3.5 1l2.5 3-1.5 2a9 9 0 0 0 5 5l2-1.5 3 2.5-1.5 2.5C7 15 1 9 1 2.5z"/></svg></li>
        <li>907 215 6630
          <svg viewBox="0 0 16 16"><path d="M4 0h8a1 1 0 0 1 1 1v14a1 1 0 0 1-1 1H4a1 1 0 0 1-1-1V1a1 1 0 0 1 1-1zm1 2v10h6V2zm3 11a1 1 0 1 0 0 2 1 1 0 0 0 0-2z"/></svg></li>
        <li>374 552 1089
          <svg viewBox="0 0 16 16"><path d="M4 1h8v4H4zM1 6h14v6h-2v3H3v-3H1zm4 4v3h6v-3z"/></svg></li>
        <li>owen@larchfield.com
          <svg viewBox="0 0 16 16"><path d="M1 3h14v10H1zm1.5 1.2L8 8.5l5.5-4.3z"/></svg></li>
        <li>www.larchfield.com
          <svg viewBox="0 0 16 16"><path d="M8 1a7 7 0 1 0 0 14A7 7 0 0 0 8 1zm-2 3h3l1 2-2 1-1 2 1 2-1 2-2-3V7zm5 5l2 1-1 3-2-1z"/></svg></li>
      </ul>
    </div>
  </section>
</body>
</html>
```